Tin Lantern "Cold Harbor" New Single Cover

Create cover artwork for the band Tin Lantern' new single "Cold Harbor" being released early 2020. Style, font and graphics to be consistent with band's previous releases and overall brand identity. Visit www.tinlanternband.example and our Spotify page https://listen.tunevault.example/artist/8QXzrT4LmNbW2cPd7KeYjA?si=HVkR3sTpZ9wLqYb2nMcXuE to view our previous releases and overall brand identity. Some examples attached as well. We are looking for someone to work with on future projects as well.

Lyrics are here: https://pages.draftbox.example/document/d/7KpRw2mXn_9LqTe4Zs8Vd_HyjB2cF5t03Qa71nRkwLpY/edit

Music is here: https://wavecrate.example/tinlantern/cold-harbor/s-rbmtx

Font styles to use
Sans Serif

Colors

Designer to choose colors to be used in the design.

Requirements
Must have
• Must be consistent with current brand identity and with prior album / single art.

```html
<!DOCTYPE html>
<html lang="en">
<head>
<meta charset="utf-8">
<title>Tin Lantern – Cold Harbor</title>
<link rel="stylesheet" href="https://fonts.googleapis.com/css2?family=Montserrat:wght@300;700&display=swap">
<style>
  :root {
    --navy: #1f2c58;
    --teal: #21a6ab;
    --gold: #fbb01b;
    --white: #ffffff;
  }
  html, body {
    margin: 0;
    padding: 0;
    overflow: hidden;
    background: var(--navy);
  }
  .cover {
    position: relative;
    width: 1200px;
    height: 1200px;
    background: var(--navy);
    overflow: hidden;
  }
  .cover-art {
    position: absolute;
    inset: 0;
  }
  .bar { fill: var(--teal); }
  .title {
    font-family: "Montserrat", sans-serif;
    font-weight: 700;
    font-size: 100px;
  }
  .title-main { fill: var(--gold); }
  .title-reflection { fill: var(--teal); }
  .band-name {
    position: absolute;
    left: 0;
    right: 0;
    top: 980px;
    margin: 0;
    text-align: center;
    font-family: "Montserrat", sans-serif;
    font-weight: 300;
    font-size: 50px;
    line-height: 56px;
    letter-spacing: 6px;
    color: var(--white);
  }
  .band-name span { display: block; }
</style>
</head>
<body>
  <main class="cover">
    <svg class="cover-art" width="1200" height="1200" viewBox="0 0 1200 1200" aria-hidden="true">
      <g class="top-bars">
        <rect class="bar" x="535" y="0" width="33" height="378"/>
        <rect class="bar" x="632" y="0" width="32" height="204"/>
      </g>
      <g class="title-reflection-group">
        <text class="title title-reflection" x="248" y="613" textLength="694" lengthAdjust="spacingAndGlyphs"
              transform="translate(0 1226) scale(1 -1)">COLD HARBOR</text>
        <rect class="bar" x="250" y="640" width="15" height="220"/>
        <rect class="bar" x="300" y="640" width="16" height="129"/>
      </g>
      <text class="title title-main" x="248" y="613" textLength="694" lengthAdjust="spacingAndGlyphs">COLD HARBOR</text>
    </svg>
    <h1 class="band-name"><span>TIN</span><span>LANTERN</span></h1>
  </main>
</body>
</html>
```